Marvel Brookworks highend custom homes

We build high end custom homes and timber frames we specialize in rustic hand made designs along with iron and concrete accents to add a modern touch 90% of my homes are buit on lake front properries attached is my logo and slogan as of now and my previous one

Target Market(s)

High end custom homes

Industry/Entity Type

Custom residential construction

Contact Information for Business Card

Been in buissness 8+ years inssured and reliable

Colors
A7469A
B969AE
D3A5CF
EDDBEB
F8F0F9

Requirements
Must have
• Must have slogan and phone number
Should not have
• A combination of rustic yet modern accents

```html
<!DOCTYPE html>
<html lang="en">
<head>
<meta charset="utf-8">
<title>Marvel Brookworks – Business Card</title>
<link href="https://fonts.googleapis.com/css2?family=Open+Sans:wght@400;600;700;800&display=swap" rel="stylesheet">
<style>
  :root {
    --bg: #d8d8d8;
    --forest: #4e6049;
    --forest-deep: #44553f;
    --amber: #e39a4a;
    --paper: #ffffff;
    --ink: #3a3a3a;
    --ink-soft: #5a5a5a;
  }
  * { box-sizing: border-box; margin: 0; padding: 0; }
  html, body { width: 696px; height: 1200px; overflow: hidden; }
  body {
    background: var(--bg);
    font-family: "Open Sans", Arial, sans-serif;
    position: relative;
  }
  .card {
    position: absolute;
    left: 58px;
    width: 580px;
    height: 330px;
    overflow: hidden;
    box-shadow: 0 10px 26px rgba(0,0,0,.22);
  }
  .card--front { top: 190px; background: var(--paper); }
  .card--back  { top: 680px; background: var(--forest); }

  .card__shape { position: absolute; inset: 0; }

  .brand {
    position: absolute;
    text-align: center;
    color: var(--paper);
  }
  .card--front .brand { left: 8px; top: 112px; width: 226px; }
  .brand__mark {
    width: 58px; height: 58px;
    margin: 0 auto 14px;
    background: var(--paper);
  }
  .brand__name {
    font-weight: 700;
    font-size: 14.5px;
    letter-spacing: .6px;
    text-transform: uppercase;
    white-space: nowrap;
  }
  .brand__slogan {
    display: flex; align-items: center; justify-content: center; gap: 6px;
    margin-top: 4px;
    font-size: 7.5px;
    letter-spacing: 1px;
    text-transform: uppercase;
    white-space: nowrap;
  }
  .brand__slogan::before, .brand__slogan::after {
    content: ""; width: 12px; height: 1px; background: currentColor;
  }

  .contact { position: absolute; left: 320px; top: 92px; color: var(--ink); }
  .contact__name { font-weight: 700; font-size: 20px; color: var(--ink); }
  .contact__role { font-size: 12px; color: var(--ink-soft); margin-top: 2px; }
  .contact__list { list-style: none; margin-top: 22px; }
  .contact__item {
    display: flex; align-items: center; gap: 10px;
    font-size: 12.5px; color: var(--ink-soft); line-height: 24px;
  }
  .contact__icon { width: 13px; height: 13px; flex: none; }

  .card--back .brand { left: 0; right: 0; top: 92px; }
  .card--back .brand__mark {
    width: 96px; height: 96px; margin-bottom: 22px;
    background: var(--forest-deep);
  }
  .card--back .brand__name { font-size: 22px; letter-spacing: 1px; }
  .card--back .brand__slogan { font-size: 10px; }
</style>
</head>
<body>

<section class="card card--front">
  <svg class="card__shape" viewBox="0 0 580 330" aria-hidden="true">
    <path d="M0 0 H180 C262 60 270 270 180 330 H0 Z" fill="var(--forest)"/>
    <path d="M193 0 C277 60 285 270 194 330" fill="none" stroke="var(--amber)" stroke-width="3"/>
  </svg>
  <div class="brand">
    <div class="brand__mark"></div>
    <div class="brand__name">Marvel Brookworks</div>
    <div class="brand__slogan">Crafted by the lakeshore</div>
  </div>
  <div class="contact">
    <div class="contact__name">Daniel Hartley</div>
    <div class="contact__role">CEO</div>
    <ul class="contact__list">
      <li class="contact__item">
        <svg class="contact__icon" viewBox="0 0 24 24"><path fill="var(--ink-soft)" d="M6.6 10.8a15 15 0 0 0 6.6 6.6l2.2-2.2c.3-.3.7-.4 1-.2 1.1.4 2.3.6 3.6.6.6 0 1 .4 1 1V20c0 .6-.4 1-1 1A17 17 0 0 1 3 4c0-.6.4-1 1-1h3.5c.6 0 1 .4 1 1 0 1.3.2 2.5.6 3.6.1.3 0 .7-.2 1z"/></svg>
        5550 123 476
      </li>
      <li class="contact__item">
        <svg class="contact__icon" viewBox="0 0 24 24"><rect x="2" y="5" width="20" height="14" rx="2" fill="var(--ink-soft)"/><path d="M3 6l9 7 9-7" fill="none" stroke="#fff" stroke-width="1.8"/></svg>
        info@marvelbrookworks.com
      </li>
      <li class="contact__item">
        <svg class="contact__icon" viewBox="0 0 24 24"><circle cx="12" cy="12" r="10" fill="var(--ink-soft)"/><path d="M2 12h20M12 2c3 3 3 17 0 20M12 2c-3 3-3 17 0 20" fill="none" stroke="#fff" stroke-width="1.4"/></svg>
        www.marvelbrookworks.com
      </li>
    </ul>
  </div>
</section>

<section class="card card--back">
  <div class="brand">
    <div class="brand__mark"></div>
    <div class="brand__name">Marvel Brookworks</div>
    <div class="brand__slogan">Crafted by the lakeshore</div>
  </div>
</section>

</body>
</html>
```